Icons, one page design and banners

Need multiple icons and banners for our platform products, like SMS marketing. And need a search results page designed for our product. It's a scan tool and we want to graphically show the results.

```html
<!DOCTYPE html>
<html lang="en">
<head>
<meta charset="utf-8">
<title>Website Vulnerability Scanner Report</title>
<link rel="stylesheet" href="https://fonts.googleapis.com/css2?family=Roboto+Condensed:wght@400;700&family=Roboto:wght@400;500;700&display=swap">
<style>
:root{
  --ink:#333;
  --muted:#555;
  --dark:#3a3d42;
  --panel:#f8f8f6;
  --stripe:#ececea;
  --line:#dcdcdc;
  --blue:#0b8ef0;
  --orange:#fb8a2c;
  --red:#e21b1b;
  --barblue:#4a8ccb;
  --green:#6cab3c;
}
*{box-sizing:border-box;margin:0;padding:0}
html,body{width:1200px;height:1200px;overflow:hidden;background:#fff}
body{position:relative;font-family:"Roboto",Arial,sans-serif;color:var(--ink);font-size:7px}
.abs{position:absolute}
.deco{position:absolute;left:0;top:0}
.title{left:445px;top:8px;font-family:"Roboto Condensed",Arial Narrow,sans-serif;font-weight:700;font-size:21px;line-height:22px;color:#2f3237}
.subtitle{left:445px;top:60px;font-size:8.5px;color:var(--muted)}
.compare{left:442px;top:78px;width:364px}
.compare .head{height:14px;background:var(--dark);color:#fff;display:flex;align-items:center;font-size:7px}
.compare .row{height:23.3px;display:flex;align-items:center;background:var(--panel);border-bottom:1px solid #e6e6e6;box-shadow:inset 18px 0 0 var(--stripe)}
.cell-area{padding-left:22px;width:156px}
.cell-light{width:107px;text-align:center;font-size:12px}
.cell-full{width:107px;text-align:center;font-size:12px}
.head .cell-light,.head .cell-full{font-size:7px}
.tick{color:var(--green);font-weight:700}
.cross{color:var(--red);font-weight:700}
.pro-btn{left:466px;top:272px;width:110px;height:26px;background:var(--blue);color:#fff;border-radius:5px;font-weight:700;font-size:9px;display:flex;align-items:center;justify-content:center}
.pro-note{left:580px;top:280px;font-size:6.8px;color:var(--blue)}
.section-head{position:absolute;left:442px;width:364px;background:var(--dark);color:#fff;font-weight:700;padding-left:22px;display:flex;align-items:center}
.panel{position:absolute;left:442px;width:364px;background:var(--panel);border:1px solid var(--line);border-top:none;box-shadow:inset 18px 0 0 var(--stripe)}
.label-blue{color:var(--blue);font-weight:500}
.pill{display:inline-block;border-radius:4px;color:#fff;font-weight:700;text-align:center;height:11px;line-height:11px;font-size:6.5px}
.bar{position:absolute;left:495px;height:11px;border-radius:4px;color:#fff;font-weight:700;font-size:6.5px;text-align:right;padding-right:6px;line-height:11px}
.t{position:absolute;left:464px;font-size:6.8px;line-height:9px}
.frow{position:absolute;left:442px;width:364px;height:18px;border-bottom:1px solid var(--line);display:flex;align-items:center;padding-left:22px;font-size:6.6px;background:var(--panel)}
.frow.title-row{font-weight:700;padding-left:24px;background:#fff}
.frow.details{color:var(--red);font-size:6px}
.col{position:absolute}
.bullets{left:452px;top:895px}
.bullets li{list-style:none;height:18px;display:flex;align-items:center;font-weight:700;font-size:6.6px}
.bullets li::before{content:"";width:7px;height:7px;border-radius:50%;background:var(--blue);margin-right:7px}
.cov{position:absolute;left:466px;font-size:6.6px;color:#444}
</style>
</head>
<body>

<svg class="deco" width="1200" height="1200" aria-hidden="true">
  <defs>
    <linearGradient id="slab" x1="0" y1="0" x2="0" y2="1">
      <stop offset="0" stop-color="#55585d"/>
      <stop offset="1" stop-color="#24272b"/>
    </linearGradient>
  </defs>
  <polygon points="706,6 828,6 808,57 688,57" fill="url(#slab)"/>
  <polygon points="420,1118 442,1118 442,1192 568,1192 565,1200 420,1200" fill="url(#slab)"/>
</svg>

<div class="abs title">Website Vulnerability<br>Scanner Report</div>
<div class="abs subtitle">Perform in-depth website scanning and discover high risk vulnerabilities.</div>

<div class="abs compare">
  <div class="head"><div class="cell-area">Testing areas</div><div class="cell-light">Light scan</div><div class="cell-full">Full scan</div></div>
  <div class="row"><div class="cell-area">Website fingerprinting</div><div class="cell-light tick">✓</div><div class="cell-full tick">✓</div></div>
  <div class="row"><div class="cell-area">Version-based vulnerability detection</div><div class="cell-light tick">✓</div><div class="cell-full tick">✓</div></div>
  <div class="row"><div class="cell-area">Common configuration issues</div><div class="cell-light tick">✓</div><div class="cell-full tick">✓</div></div>
  <div class="row"><div class="cell-area">SQL injection</div><div class="cell-light cross">✕</div><div class="cell-full tick">✓</div></div>
  <div class="row"><div class="cell-area">Cross-Site Scripting</div><div class="cell-light cross">✕</div><div class="cell-full tick">✓</div></div>
  <div class="row"><div class="cell-area">Remote command execution</div><div class="cell-light cross">✕</div><div class="cell-full tick">✓</div></div>
  <div class="row"><div class="cell-area">Discover sensitive files</div><div class="cell-light cross">✕</div><div class="cell-full tick">✓</div></div>
</div>

<div class="abs pro-btn">Geta PRO Account</div>
<div class="abs pro-note">to unlock the full capabilities of this scanner!</div>

<!-- Summary -->
<div class="section-head" style="top:306px;height:16px;font-size:9.5px">SUMMARY</div>
<div class="panel" style="top:322px;height:185px"></div>
<div class="t label-blue" style="top:327px">Overall risk level:</div>
<div class="abs pill" style="left:520px;top:326px;width:57px;background:var(--orange)">Medium</div>
<div class="t label-blue" style="top:346px">Risk ratings:</div>
<div class="t" style="top:359px">High:</div>
<div class="t" style="top:373px">Medium:</div>
<div class="t" style="top:387px">Low:</div>
<div class="t" style="top:401px">Info:</div>
<div class="bar" style="top:358px;width:18px;background:var(--red);text-align:center;padding:0">0</div>
<div class="bar" style="top:372px;width:53px;background:var(--orange);padding-right:8px">1</div>
<div class="bar" style="top:386px;width:205px;background:var(--barblue)">4</div>
<div class="bar" style="top:400px;width:232px;background:var(--green)">5</div>
<div class="t label-blue" style="top:419px">Scan information:</div>
<div class="t" style="top:434px">Start time:</div><div class="t" style="top:434px;left:518px">2018-10-27 16:42:22</div>
<div class="t" style="top:448px">Finish time:</div><div class="t" style="top:448px;left:518px">2018-10-27 16:42:25</div>
<div class="t" style="top:462px">Scan duration:</div><div class="t" style="top:462px;left:518px">3 sec</div>
<div class="t" style="top:476px">Tests performed: 10/10</div>
<div class="t" style="top:490px">Scan status:</div>
<div class="abs pill" style="left:511px;top:488px;width:51px;height:12px;line-height:12px;background:var(--green)">Finished</div>

<!-- Findings -->
<div class="section-head" style="top:515px;height:15px;font-size:9.5px">FINDINGS</div>
<div class="panel" style="top:530px;height:355px;box-shadow:none"></div>
<div class="frow title-row" style="top:532px">Insecure HTTP cookies</div>
<div class="frow" style="top:550px">Cookie Name<span class="col" style="left:147px">Flags missing</span></div>
<div class="frow" style="top:568px">SHOP_PREF<span class="col" style="left:147px">Secure, HttpOnly</span></div>
<div class="frow" style="top:586px">SESS_ID<span class="col" style="left:147px">Secure</span></div>
<div class="frow details" style="top:604px">| Details |</div>
<div class="frow title-row" style="top:622px">Server software and technology found</div>
<div class="frow" style="top:640px">Software / Version<span class="col" style="left:93px">Category</span></div>
<div class="frow" style="top:658px;padding-left:24px">Northwind Web Server<span class="col" style="left:93px">Web Servers</span></div>
<div class="frow details" style="top:676px">| Details |</div>
<div class="frow title-row" style="top:694px;padding-left:22px">Missing HTTP security headers</div>
<div class="frow" style="top:712px">HTTP Security Header<span class="col" style="left:129px">Header Role</span><span class="col" style="left:308px">Status</span></div>
<div class="frow" style="top:730px">X-Content-Type-Options<span class="col" style="left:129px">Prevents possible phishing or XSS attacks</span><span class="col" style="left:308px">Not set</span></div>
<div class="frow details" style="top:748px">| Details |</div>
<div class="frow title-row" style="top:766px">Redirect from HTTP to HTTPS</div>
<div class="frow" style="top:784px;height:28px;border-bottom:none;line-height:11px">http://www.northwind-mart.com redirects to:<br>https://www.northwind-mart.com/?src=ssl</div>
<div class="frow details" style="top:812px;height:16px">| Details |</div>
<div class="frow title-row" style="top:828px">Robots.txt file found</div>
<div class="frow" style="top:846px;border-bottom:none">http://www.northwind-mart.com/robots.txt</div>
<div class="frow details" style="top:864px;border-bottom:none">| Details |</div>

<ul class="abs bullets">
  <li>No vulnerabilities found for server-side software</li>
  <li>No security issue found regarding client access policies</li>
  <li>Directory listing not found (quick scan)</li>
  <li>No password input found (auto-complete test)</li>
  <li>No password input found (clear-text submission test)</li>
</ul>

<!-- Coverage -->
<div class="section-head" style="top:992px;height:14px;font-size:7.5px">SCAN COVERAGE INFORMATION</div>
<div class="panel" style="top:1006px;height:186px;box-shadow:none"></div>
<div class="cov" style="left:464px;top:1013px;font-weight:700;color:var(--ink)">List of tests performed (10/10)</div>
<div class="cov" style="top:1025px">Fingerprinting the server software and technology...</div>
<div class="cov" style="top:1037px">Checking for vulnerabilities of server-side software...</div>
<div class="cov" style="top:1049px">Analyzing the security of HTTP cookies...</div>
<div class="cov" style="top:1061px">Analyzing HTTP security headers...</div>
<div class="cov" style="top:1073px">Checking for secure communication...</div>
<div class="cov" style="top:1085px">Checking robots.txt file...</div>
<div class="cov" style="top:1097px">Checking client access policies...</div>
<div class="cov" style="top:1109px">Checking for directory listing (quick scan)...</div>
<div class="cov" style="top:1121px">Checking for password auto-complete (quick scan)...</div>
<div class="cov" style="top:1133px">Checking for clear-text submission of passwords (quick scan)...</div>
<div class="cov" style="left:464px;top:1150px;font-weight:700;color:var(--ink)">Scan parameters</div>
<div class="cov" style="left:464px;top:1163px">Website URL:&nbsp;&nbsp; http://www.northwind-mart.com</div>
<div class="cov" style="left:464px;top:1176px">Scan type:&nbsp;&nbsp;&nbsp;&nbsp;&nbsp;&nbsp; Light</div>

</body>
</html>
```